Vantorel Business Card

I want a business card for me and my employees.
On one side it must be in Greek and on the other side in English. The color must much the one of the logo

Target Market(s)

Customers that are looking for security and antipiracy advisors

Contact Information for Business Card

Title, Email, Phone, website , Mobile Address Zip code, city and country

Requirements
Must have
• The colors of our logo (the blue ones)

```html
<!DOCTYPE html>
<html lang="en">
<head>
<meta charset="utf-8">
<title>Vantorel Advisory Business Card</title>
<link rel="stylesheet" href="https://fonts.googleapis.com/css2?family=Roboto:wght@300;400;500;700&display=swap">
<style>
  :root {
    --page-bg: #f0f0f0;
    --brand-navy: #27235c;
    --card-white: #fafafa;
    --card-border: #3a3a3a;
    --text-muted: #5c5c66;
    --text-on-navy: #ffffff;
    --muted-on-navy: #c9c7e4;
    --url-faint: #6d6a96;
  }
  html, body {
    margin: 0;
    padding: 0;
    width: 1200px;
    height: 1052px;
    overflow: hidden;
    background: var(--page-bg);
    font-family: "Roboto", Arial, sans-serif;
  }
  .canvas {
    position: relative;
    width: 1200px;
    height: 1052px;
  }
  .card {
    position: absolute;
    left: 324px;
    width: 552px;
    box-sizing: border-box;
  }
  .card--greek {
    top: 142px;
    height: 333px;
    background: var(--brand-navy);
  }
  .card--english {
    top: 546px;
    height: 334px;
    background: var(--card-white);
    border: 1px solid var(--card-border);
  }

  /* Wordmark */
  .brand {
    position: absolute;
    left: 0;
    right: 0;
    display: flex;
    justify-content: center;
    align-items: center;
    gap: 14px;
  }
  .brand__square {
    width: 62px;
    height: 62px;
    background: currentColor;
  }
  .brand__name {
    font-weight: 700;
    line-height: 1;
    text-transform: uppercase;
  }
  .brand__name span { display: block; }
  .brand__line-main { font-size: 44px; letter-spacing: 0; }
  .brand__line-sub { font-size: 24px; letter-spacing: 4.6px; margin-top: 6px; }
  .card--greek .brand { top: 34px; color: var(--text-on-navy); }
  .card--english .brand { top: 52px; color: var(--brand-navy); }

  /* Contact block */
  .contact {
    position: absolute;
    left: 0;
    right: 0;
    text-align: center;
  }
  .contact__name {
    margin: 0;
    font-size: 21px;
    font-weight: 700;
    line-height: 26px;
  }
  .contact__title {
    margin: 2px 0 0;
    font-size: 15px;
    font-weight: 400;
    letter-spacing: 0.4px;
    line-height: 19px;
  }
  .contact__details {
    margin: 14px 0 0;
    font-size: 14px;
    font-weight: 400;
    line-height: 17px;
  }
  .contact__details b { font-weight: 500; }
  .contact__sep { margin: 0 10px; }

  .card--english .contact { top: 174px; }
  .card--english .contact__name,
  .card--english .contact__details b { color: var(--brand-navy); }
  .card--english .contact__title,
  .card--english .contact__details { color: var(--text-muted); }

  .card--greek .contact { top: 140px; }
  .card--greek .contact__name,
  .card--greek .contact__details b { color: var(--text-on-navy); }
  .card--greek .contact__title,
  .card--greek .contact__details { color: var(--muted-on-navy); }

  .greek-url {
    position: absolute;
    left: 0;
    right: 0;
    top: 299px;
    text-align: center;
    font-size: 14px;
    font-weight: 300;
    letter-spacing: 9.4px;
    color: var(--url-faint);
  }
</style>
</head>
<body>
<main class="canvas">
  <section class="card card--greek" lang="el" aria-label="Card side in Greek">
    <div class="brand">
      <div class="brand__square"></div>
      <div class="brand__name">
        <span class="brand__line-main">Vantorel</span>
        <span class="brand__line-sub">Advisory</span>
      </div>
    </div>
    <div class="contact">
      <h2 class="contact__name">Τζον Ντόε Σμιθ</h2>
      <p class="contact__title">Διευθύνων Σύμβουλος</p>
      <p class="contact__details">
        <b>Τ</b>: 828-111-1111<span class="contact__sep">|</span><b>Κ</b>: 828-222-2222<br>
        <b>Ε</b>: john@yourwebsite.com<span class="contact__sep">|</span><b>Ι</b>: www.yourwebsite.com<br>
        Οδός Οπουδήποτε 234, Οποιαδήποτε Πόλη, ΗΠΑ 123456
      </p>
    </div>
    <div class="greek-url">www.vantoreladvisory.com</div>
  </section>

  <section class="card card--english" lang="en" aria-label="Card side in English">
    <div class="brand">
      <div class="brand__square"></div>
      <div class="brand__name">
        <span class="brand__line-main">Vantorel</span>
        <span class="brand__line-sub">Advisory</span>
      </div>
    </div>
    <div class="contact">
      <h1 class="contact__name">John Doe Smith</h1>
      <p class="contact__title">Managing Director</p>
      <p class="contact__details">
        <b>P</b>: 828-111-1111<span class="contact__sep">|</span><b>M</b>: 828-222-2222<br>
        <b>E</b>: john@yourwebsite.com<span class="contact__sep">|</span><b>W</b>: www.yourwebsite.com<br>
        234 Anywhere St., Any City, Any Town, US 123456
      </p>
    </div>
  </section>
</main>
</body>
</html>
```